Silver Birch Decorators Banner

Create a banner that displays and reinforces Silver Birch Decorators’ brand identity while promoting our interior painting services. The banner will be displayed at indoor venues through the winter. The design should be clean, professional, and visually recognizable to both new and returning customers. See attached design brief & logo source files.

```html
<!DOCTYPE html>
<html lang="en">
<head>
<meta charset="utf-8">
<title>Silver Birch Decorators – Interior Painting Banner</title>
<link rel="stylesheet" href="https://fonts.googleapis.com/css2?family=Anton&family=Poppins:wght@600;700;800&display=swap">
<style>
  :root {
    --page-bg: #a6aba8;
    --board-dark: #1c1c1c;
    --board-mid: #3d3d3d;
    --brand-green: #95c970;
    --url-green: #6b9a4e;
    --ink: #1e1e1e;
    --white: #ffffff;
    --divider: #8a8a8a;
  }
  html, body {
    margin: 0;
    width: 1200px;
    height: 600px;
    overflow: hidden;
    background: var(--page-bg);
  }
  .banner {
    position: absolute;
    left: 30px;
    top: 72px;
    width: 1140px;
    height: 456px;
    display: block;
  }
  .headline { font-family: "Anton", "Oswald", sans-serif; fill: var(--white); font-size: 148px; }
  .tagline { font-family: "Poppins", sans-serif; font-weight: 700; fill: var(--ink); font-size: 30px; }
  .brand-name { font-family: "Poppins", sans-serif; font-weight: 700; fill: var(--white); }
  .service-label { font-family: "Poppins", sans-serif; font-weight: 700; fill: var(--white); font-size: 32px; text-anchor: middle; }
  .divider { stroke: var(--divider); stroke-width: 1; stroke-dasharray: 4 3; }
  .icon-green { fill: var(--brand-green); }
  .icon-white { fill: var(--white); }
  .cta-text { font-family: "Poppins", sans-serif; font-weight: 700; fill: var(--ink); font-size: 33px; }
  .url { font-family: "Poppins", sans-serif; font-weight: 700; font-size: 44px; fill: var(--ink); }
  .url-name { fill: var(--url-green); }
</style>
</head>
<body>
<svg class="banner" viewBox="0 0 1140 456" xmlns="http://www.w3.org/2000/svg" aria-label="Silver Birch Decorators interior painting banner">
  <defs>
    <radialGradient id="board-glow" cx="0.5" cy="0.55" r="0.7">
      <stop offset="0" stop-color="var(--board-mid)"/>
      <stop offset="1" stop-color="var(--board-dark)"/>
    </radialGradient>
  </defs>

  <rect class="board" width="1140" height="456" fill="url(#board-glow)" role="img" aria-label="Dark charcoal wood-grain background"/>

  <!-- Headline -->
  <text class="headline" x="44" y="155" textLength="726" lengthAdjust="spacingAndGlyphs">PAINT SMARTER</text>

  <!-- Tagline pill -->
  <rect x="47" y="171" width="723" height="49" rx="12" fill="var(--brand-green)"/>
  <text class="tagline" x="76" y="207" textLength="662" lengthAdjust="spacing">INTERIOR PAINTING SERVICES</text>

  <!-- Brand name -->
  <circle cx="951" cy="80" r="34" fill="var(--brand-green)"/>
  <text class="brand-name" x="951" y="160" font-size="40" text-anchor="middle" textLength="296" lengthAdjust="spacingAndGlyphs">SILVER BIRCH</text>
  <text class="brand-name" x="951" y="210" font-size="40" text-anchor="middle" textLength="296" lengthAdjust="spacingAndGlyphs">DECORATORS</text>

  <!-- Services row -->
  <g class="services">
    <!-- Walls -->
    <g class="icon-walls">
      <path class="icon-green" d="M82 240h44v12h-32v40h-12z"/>
      <rect class="icon-white" x="95" y="256" width="32" height="11" rx="2"/>
      <rect class="icon-white" x="108" y="267" width="4" height="9"/>
      <rect class="icon-green" x="107" y="276" width="6" height="16" rx="2"/>
    </g>
    <text class="service-label" x="104" y="327">Walls</text>

    <line class="divider" x1="184" y1="239" x2="184" y2="334"/>

    <!-- Ceilings -->
    <g class="icon-ceilings">
      <rect class="icon-white" x="256" y="241" width="55" height="9" rx="2"/>
      <rect class="icon-green" x="282" y="250" width="3" height="12"/>
      <path class="icon-green" d="M261 282 Q283 258 305 282z"/>
      <path class="icon-green" d="M276 285 a7 5 0 0 0 14 0z"/>
    </g>
    <text class="service-label" x="283" y="327">Ceilings</text>

    <line class="divider" x1="382" y1="239" x2="382" y2="334"/>

    <!-- Trim -->
    <g class="icon-trim">
      <rect class="icon-green" x="443" y="241" width="24" height="50"/>
      <rect x="447" y="245" width="16" height="44" fill="none" stroke="var(--board-dark)" stroke-width="1.5"/>
      <rect x="449" y="266" width="2" height="6" fill="var(--board-dark)"/>
      <rect class="icon-white" x="439" y="291" width="33" height="3"/>
    </g>
    <text class="service-label" x="455" y="327">Trim</text>

    <line class="divider" x1="531" y1="239" x2="531" y2="334"/>

    <!-- Cabinets -->
    <g class="icon-cabinets">
      <rect class="icon-green" x="617" y="242" width="23" height="20" rx="2"/>
      <rect class="icon-green" x="643" y="242" width="21" height="20" rx="2"/>
      <rect class="icon-white" x="617" y="265" width="23" height="18" rx="2"/>
      <rect class="icon-green" x="643" y="265" width="21" height="18" rx="2"/>
      <rect x="623" y="253" width="9" height="3" rx="1.5" fill="var(--board-dark)"/>
      <rect x="648" y="253" width="9" height="3" rx="1.5" fill="var(--board-dark)"/>
      <rect x="624" y="270" width="3" height="6" rx="1.5" fill="var(--board-dark)"/>
      <rect x="629" y="270" width="3" height="6" rx="1.5" fill="var(--board-dark)"/>
      <rect x="648" y="271" width="9" height="3" rx="1.5" fill="var(--board-dark)"/>
    </g>
    <text class="service-label" x="639" y="327">Cabinets</text>

    <line class="divider" x1="752" y1="239" x2="752" y2="334"/>

    <!-- Repair -->
    <g class="icon-repair">
      <rect class="icon-green" x="830" y="243" width="20" height="49" rx="2"/>
      <path class="icon-white" d="M820 248 L842 268 L828 282 L814 270z"/>
      <path class="icon-green" d="M818 276 L826 284 L814 294 Q806 294 808 286z"/>
    </g>
    <text class="service-label" x="838" y="327">Repair</text>

    <line class="divider" x1="928" y1="239" x2="928" y2="334"/>

    <!-- Access -->
    <g class="icon-access" fill="none" stroke="var(--brand-green)" stroke-width="3">
      <rect class="icon-white" x="1006" y="240" width="34" height="5" stroke="none"/>
      <rect x="1010" y="248" width="26" height="42"/>
      <line x1="1010" y1="262" x2="1036" y2="262"/>
      <line x1="1010" y1="276" x2="1036" y2="276"/>
      <path d="M1010 248 L1036 262 M1036 248 L1010 262 M1010 262 L1036 276 M1036 262 L1010 276 M1010 276 L1036 290 M1036 276 L1010 290"/>
      <line x1="1006" y1="291" x2="1040" y2="291"/>
    </g>
    <text class="service-label" x="1023" y="327">Access</text>
  </g>

  <!-- Call to action -->
  <rect x="43" y="358" width="560" height="63" rx="31.5" fill="var(--brand-green)"/>
  <rect x="514" y="358" width="572" height="63" rx="31.5" fill="var(--white)"/>
  <text class="cta-text" x="69" y="402" textLength="423" lengthAdjust="spacingAndGlyphs">Book a Free Estimate at</text>

  <g class="icon-globe" fill="none" stroke="var(--url-green)" stroke-width="2.6">
    <circle cx="545" cy="390" r="12"/>
    <ellipse cx="545" cy="390" rx="5" ry="12"/>
    <line x1="533" y1="386" x2="557" y2="386"/>
    <line x1="533" y1="394" x2="557" y2="394"/>
  </g>

  <text class="url" x="589" y="403" textLength="482" lengthAdjust="spacingAndGlyphs">www.<tspan class="url-name">silverbirchdeco</tspan>.com</text>
</svg>
</body>
</html>
```